Label design for Essential Oil Bottle

We need a logo and label design for our range of medical essential oils. We distill our own oils in very stringent conditions and run various analysis per batch. That is what sets us apart from other essential oil retailers. Our brand name is 'Velmiro', which is the shortened name for Sacred Frankincense.

The design should communicate the following qualities:

1. Nature
2. Clinical
3. Professional
4. Advanced

Please keep the design minimal and clean.

We like the colours gold, maroon, white. Essential oil bottle will be 15 ml amber bottle

Types of oil: Orange, Rose, Frankincense, Myrrh

Do keep in mind that this same brand will also have a range of skin care.
Updates

Hi all,

Just a reminder that the label should be landscape and not portrait. The label is meant to wrap around the 15 ml amber bottle. Photo of the bottle is attached in the brief.

thanksĀ 

Target Market(s)

Clinicians, Laboratories, General public

Industry/Entity Type

Medical

Requirements
Must have
• Front:

Logo
Oil name
Latin name (in smaller italized font)
Volume: 0.5 oz/15 ml

Back:

Barcode
Batch code
Expiry date
Company name/address: Velmiro Inc. 5817 Harlow Ln, Los Angeles, CA

```html
<!DOCTYPE html>
<html lang="en">
<head>
<meta charset="utf-8">
<title>Velmiro – Medical Essential Oil Labels</title>
<link rel="stylesheet" href="https://fonts.googleapis.com/css2?family=Quicksand:wght@400;500&family=Cormorant+Garamond:ital,wght@1,500&display=swap">
<style>
  :root {
    --backdrop: #b5b5b5;
    --label-white: #fbfbf9;
    --gold: #c4a649;
    --gold-light: #dcc679;
    --gold-dark: #a98b35;
    --ink: #4b4a47;
    --ink-soft: #6e6c66;
  }
  * { margin: 0; padding: 0; box-sizing: border-box; }
  html, body {
    width: 1200px; height: 1200px; overflow: hidden;
    background: var(--backdrop);
    font-family: "Quicksand", sans-serif;
    color: var(--ink);
  }
  .label-sheet {
    position: absolute; left: 100px; top: 72px;
    width: 1000px;
    display: flex; flex-direction: column; gap: 32px;
  }
  .label {
    position: relative;
    height: 240px;
    background: var(--label-white);
    box-shadow: 0 2px 6px rgba(0,0,0,0.12);
  }
  .label-front {
    position: absolute; left: 320px; top: 0;
    width: 360px; height: 100%;
    display: flex; flex-direction: column; align-items: center;
    padding-top: 22px;
  }
  .brand {
    display: flex; align-items: center; gap: 10px;
    font-size: 26px; font-weight: 500; letter-spacing: 3px;
    color: var(--gold);
    text-transform: uppercase;
  }
  .brand-dot {
    width: 22px; height: 22px; border-radius: 50%;
    background: var(--gold);
  }
  .range-title {
    margin-top: 14px;
    font-size: 22px; font-weight: 500; color: var(--ink);
  }
  .oil-band {
    margin-top: 8px;
    width: 300px; height: 74px;
    background: linear-gradient(90deg, var(--gold-dark), var(--gold-light) 50%, var(--gold-dark));
    display: flex; flex-direction: column; align-items: center; justify-content: center;
  }
  .oil-name { font-size: 26px; font-weight: 400; color: var(--label-white); line-height: 1.1; }
  .oil-latin {
    font-family: "Cormorant Garamond", serif; font-style: italic; font-weight: 500;
    font-size: 17px; color: #f3ead0;
  }
  .volume { margin-top: 12px; font-size: 16px; font-weight: 500; color: var(--ink); }
  .label-back {
    position: absolute; left: 720px; top: 0;
    width: 240px; height: 100%;
    display: flex; flex-direction: column; align-items: center;
    padding-top: 40px;
  }
  .seal {
    width: 64px; height: 64px; border-radius: 50%;
    border: 2px solid var(--gold);
  }
  .origin-tag {
    margin-top: 18px;
    width: 110px; height: 48px;
    background: linear-gradient(90deg, var(--gold-dark), var(--gold-light) 50%, var(--gold-dark));
    display: flex; align-items: center; justify-content: center; text-align: center;
    font-family: "Cormorant Garamond", serif; font-style: italic; font-weight: 500;
    font-size: 14px; line-height: 1.05; color: var(--label-white);
  }
  .maker {
    margin-top: 14px;
    font-size: 11px; line-height: 1.3; color: var(--ink-soft); text-align: left;
    width: 150px;
  }
</style>
</head>
<body>
<main class="label-sheet">

  <section class="label">
    <div class="label-front">
      <div class="brand"><span class="brand-dot"></span>Velmiro</div>
      <p class="range-title">medical esential oil</p>
      <div class="oil-band"><span class="oil-name">rose</span><span class="oil-latin">rosa damascena</span></div>
      <p class="volume">℮ 15 ml 0.50 fl.oz.</p>
    </div>
    <div class="label-back">
      <div class="seal"></div>
      <div class="origin-tag">originally<br>from India</div>
      <p class="maker">Manufactured by:<br>Velmiro Inc. 5817 Harlow Ln<br>Los Angeles, CA</p>
    </div>
  </section>

  <section class="label">
    <div class="label-front">
      <div class="brand"><span class="brand-dot"></span>Velmiro</div>
      <p class="range-title">medical esential oil</p>
      <div class="oil-band"><span class="oil-name">frankincense</span><span class="oil-latin">boswellia carterii</span></div>
      <p class="volume">℮ 15 ml 0.50 fl.oz.</p>
    </div>
    <div class="label-back">
      <div class="seal"></div>
      <div class="origin-tag">originally<br>from India</div>
      <p class="maker">Manufactured by:<br>Velmiro Inc. 5817 Harlow Ln<br>Los Angeles, CA</p>
    </div>
  </section>

  <section class="label">
    <div class="label-front">
      <div class="brand"><span class="brand-dot"></span>Velmiro</div>
      <p class="range-title">medical esential oil</p>
      <div class="oil-band"><span class="oil-name">orange</span><span class="oil-latin">citrus sinensis</span></div>
      <p class="volume">℮ 15 ml 0.50 fl.oz.</p>
    </div>
    <div class="label-back">
      <div class="seal"></div>
      <div class="origin-tag">originally<br>from India</div>
      <p class="maker">Manufactured by:<br>Velmiro Inc. 5817 Harlow Ln<br>Los Angeles, CA</p>
    </div>
  </section>

  <section class="label">
    <div class="label-front">
      <div class="brand"><span class="brand-dot"></span>Velmiro</div>
      <p class="range-title">medical esential oil</p>
      <div class="oil-band"><span class="oil-name">myrrh</span><span class="oil-latin">commiphora myrrha</span></div>
      <p class="volume">℮ 15 ml 0.50 fl.oz.</p>
    </div>
    <div class="label-back">
      <div class="seal"></div>
      <div class="origin-tag">originally<br>from India</div>
      <p class="maker">Manufactured by:<br>Velmiro Inc. 5817 Harlow Ln<br>Los Angeles, CA</p>
    </div>
  </section>

</main>
</body>
</html>
```